Business Card for Dental Office

Our office is in the Hillcrest section of San Diego, California which is a well-established area. Maybe the back can be a map of our office location

```html
<!DOCTYPE html>
<html lang="en">
<head>
<meta charset="utf-8">
<title>Harborview Dental — Business Card</title>
<link rel="stylesheet" href="https://fonts.googleapis.com/css2?family=Jost:wght@400;500;700&display=swap">
<style>
  :root {
    --ink: #1b2290;
    --brand-grey: #8d9c9e;
    --paper: #ffffff;
  }
  * { margin: 0; padding: 0; box-sizing: border-box; }
  html, body {
    width: 1200px;
    height: 686px;
    overflow: hidden;
    background: var(--paper);
  }
  .card {
    position: relative;
    width: 1200px;
    height: 686px;
    background: var(--paper);
    font-family: "Jost", "Futura", sans-serif;
    color: var(--ink);
  }
  .brand {
    position: absolute;
    left: 282px;
    top: 383px;
    transform: translate(-50%, -50%);
    display: flex;
    align-items: center;
    gap: 12px;
    color: var(--brand-grey);
    font-weight: 500;
    font-size: 30px;
    white-space: nowrap;
  }
  .brand-dot {
    width: 14px;
    height: 14px;
    border-radius: 50%;
    background: var(--brand-grey);
  }
  .divider {
    position: absolute;
    left: 556px;
    top: 230px;
    width: 1.5px;
    height: 328px;
    background: var(--ink);
  }
  .name {
    position: absolute;
    left: 685px;
    top: 130px;
    font-size: 31px;
    font-weight: 700;
    letter-spacing: 2.5px;
    text-transform: uppercase;
  }
  .title {
    position: absolute;
    left: 687px;
    top: 182px;
    font-size: 19px;
    font-weight: 500;
    letter-spacing: 0.3px;
  }
  .rule {
    position: absolute;
    left: 730px;
    width: 233px;
    height: 2px;
    background: var(--ink);
  }
  .rule--top { top: 244px; }
  .rule--mid { top: 429px; }
  .rule--bottom { left: 732px; top: 555px; }
  .contact {
    position: absolute;
    left: 685px;
    display: flex;
    font-size: 19px;
    font-weight: 500;
    line-height: 30px;
  }
  .contact-label {
    width: 45px;
    flex: none;
  }
  .contact--phone { top: 278px; }
  .contact--email { top: 344px; }
  .contact--address { top: 458px; }
</style>
</head>
<body>
  <div class="card">
    <div class="brand">
      <span class="brand-dot"></span>
      <span class="brand-name">Harborview Dental</span>
    </div>

    <div class="divider"></div>

    <h1 class="name">Maren Caldwell</h1>
    <p class="title">DENTIST</p>

    <div class="rule rule--top"></div>

    <p class="contact contact--phone">
      <span class="contact-label">t :</span>
      <span class="contact-value">619.555.0142</span>
    </p>
    <p class="contact contact--email">
      <span class="contact-label">e :</span>
      <span class="contact-value">mcaldwell@harborviewsmiles.com</span>
    </p>

    <div class="rule rule--mid"></div>

    <p class="contact contact--address">
      <span class="contact-label">a :</span>
      <span class="contact-value">2740 Larkspur Avenue,<br>Suite 210 San Diego, CA 92103</span>
    </p>

    <div class="rule rule--bottom"></div>
  </div>
</body>
</html>
```